Design for web app with Plinkora Stratum Craft - Tarvo7 SMS consult

We are developing a web app that will work in browsers. Its main purpose is to allow for users (signing up and logging in with their phone number) to track their habbits and select consultants to whom they can send SMS for help.

The wireframes of the app can be accessed here (pdf):
https://files.plinkora.example/d/7K2mWqLzXv4NtRb9HcJpYsAeUfDg3/view

NB!: Please do not follow the mockups 100% literally, but the Plinkora Stratum craft guidelines.

The technical specifications and descriptions of the web app's functionalities are available in the link below:
https://papers.plinkora.example/doc/4HsTnV8bQeZr2LmXwYcKpDjAuFgN6oRiE5tW1yMx/edit

Requirements for the design:

- The design should be provided as PSD, where each page/section should be in its own PSD file OR all pages/sections should be represented as folder groups in a single PSD file.

- All graphical elements in the design should be delivered as single layers which can then be extracted from the PSD.

- All graphical elements (icons, graphical buttons, etc.) should be provided as vector objects in the PSD, so that they can be exported into different sizes without loss of quality (for responsiveness).

- The design should use either web safe fonts or Plinkora Type.

Instructions for the design:
The design should be based on Plinkora Stratum Craft - http://www.plinkora.example/craft/spec/stratum-craft/overview.html

Please also provide an app icon and suggest a logo for the app.

Requirements
Must have
• Based on Plinkora Stratum Craft
• Flat
Nice to have
• Nice looking and not so stiff as the default Plinkora Stratum Craft, but it is important to follow their guidelines.
Should not have
• 3D

```html
<!DOCTYPE html>
<html lang="en">
<head>
<meta charset="utf-8">
<title>Tarvo7 – Login</title>
<link rel="stylesheet" href="https://fonts.googleapis.com/css2?family=Marcellus+SC&family=Open+Sans:wght@300;400&family=Luckiest+Guy&display=swap">
<style>
  :root {
    --status-bar: #0b1f38;
    --status-ink: #ffffff;
    --bg-top: #6d4a31;
    --bg-bottom: #532808;
    --sheen: #7b5a43;
    --title-ink: #e4d9b6;
    --brand-ink: #e8ddc3;
    --field-fill: #e1d9d5;
    --field-edge: #a3834f;
    --field-ink: #1e1a18;
    --login-fill: #22150f;
    --login-edge: #8b6b3f;
    --signup-fill: #8c1210;
    --signup-edge: #b27848;
    --button-ink: #ffffff;
    --link-ink: #f2e8da;
    --divider: #e4d4c2;
  }
  * { box-sizing: border-box; margin: 0; padding: 0; }
  html, body { width: 720px; height: 1200px; overflow: hidden; background: var(--bg-bottom); }
  .screen {
    position: relative;
    width: 720px;
    height: 1200px;
    overflow: hidden;
    background: linear-gradient(180deg, var(--bg-top) 0%, #633c1f 45%, var(--bg-bottom) 100%);
    font-family: "Open Sans", Arial, sans-serif;
  }
  .sheen { position: absolute; inset: 0; width: 720px; height: 1200px; }
  .status-bar {
    position: absolute; top: 0; left: 0; width: 720px; height: 30px;
    background: var(--status-bar); color: var(--status-ink);
    font-size: 21px; line-height: 30px; text-align: center;
  }
  .status-bar .signal { position: absolute; left: 12px; top: 9px; }
  .status-bar .battery { position: absolute; right: 14px; top: 8px; }
  .brand {
    position: absolute; left: 66px; top: 80px;
    font-family: "Marcellus SC", Georgia, serif;
    font-size: 44px; line-height: 60px; color: var(--brand-ink);
    letter-spacing: 1px;
  }
  .title {
    position: absolute; left: 0; top: 340px; width: 720px; text-align: center;
    font-family: "Marcellus SC", Georgia, serif;
    font-size: 66px; line-height: 80px; color: var(--title-ink);
  }
  .field {
    position: absolute; left: 165px; width: 365px; height: 58px;
    background: var(--field-fill); border: 2px solid var(--field-edge); border-radius: 14px;
    font-size: 27px; line-height: 54px; text-align: center; color: var(--field-ink);
  }
  .field-phone { top: 462px; }
  .field-password { top: 564px; }
  .button {
    position: absolute; left: 221px; width: 232px; height: 61px;
    border-radius: 13px; border: 2px solid;
    font-family: "Luckiest Guy", Impact, sans-serif;
    font-size: 30px; line-height: 61px; text-align: center; color: var(--button-ink);
    letter-spacing: 1px;
  }
  .button-login { top: 664px; background: var(--login-fill); border-color: var(--login-edge); }
  .button-signup { top: 968px; background: var(--signup-fill); border-color: var(--signup-edge); }
  .forgot-link {
    position: absolute; left: 0; top: 752px; width: 720px; text-align: center;
    font-size: 35px; line-height: 50px; font-weight: 300; color: var(--link-ink);
    text-decoration: underline; text-underline-offset: 6px;
    text-shadow: 1px 3px 4px rgba(0,0,0,0.55);
  }
  .divider {
    position: absolute; left: 124px; top: 876px; width: 488px; height: 2px;
    background: var(--divider);
  }
</style>
</head>
<body>
<main class="screen">
  <svg class="sheen" viewBox="0 0 720 1200" aria-hidden="true">
    <path d="M360 30 C520 150 640 420 690 760 C705 880 715 1050 720 1200 L720 30 Z" fill="var(--sheen)" opacity="0.85"/>
  </svg>

  <header class="status-bar">
    <svg class="signal" width="64" height="14" viewBox="0 0 64 14" aria-hidden="true">
      <circle cx="7" cy="7" r="6" fill="#000"/>
      <circle cx="20" cy="7" r="6" fill="#000"/>
      <circle cx="33" cy="7" r="6" fill="#000"/>
      <circle cx="46" cy="7" r="6" fill="#fff"/>
    </svg>
    <span class="clock">10:00 AM</span>
    <svg class="battery" width="42" height="16" viewBox="0 0 42 16" aria-hidden="true">
      <rect x="1" y="1" width="36" height="14" fill="none" stroke="#fff" stroke-width="2"/>
      <rect x="4" y="4" width="20" height="8" fill="#fff"/>
      <rect x="38" y="5" width="3" height="6" fill="#fff"/>
    </svg>
  </header>

  <div class="brand">Tarvo7</div>

  <h1 class="title">Login</h1>

  <div class="field field-phone">Phone</div>
  <div class="field field-password">Password</div>

  <div class="button button-login">Login</div>

  <a class="forgot-link">Forgot&nbsp; your password?</a>

  <div class="divider"></div>

  <div class="button button-signup">Sign up</div>
</main>
</body>
</html>
```